Truck wrap Halvik T-720 as a rolling billboard

have multiple trucks to wrap with logo and company info as a rolling billboard.

Tarnwell Outfitters logo

Main focus are in sod

contact 555-317-4486

licensed and insured - maybe on back of truck
"Sod and Landscape Installation and Delivery" - on side of truck

Target Market(s)

landscapers and builders

Industry/Entity Type

Landscape

Font styles to use
Sans Serif

Colors
acd037

Requirements
Must have
• photo of palletized sod
555-317-4486
Nice to have
• cool way to show palletized sod

Quenlar logo that can be added or taken away from deisgn
Should not have
• no big leaf
Sod needs to be bigger than the leaf from the logo

```html
<!DOCTYPE html>
<html lang="en">
<head>
<meta charset="utf-8">
<title>Tarnwell Outfitters – Truck Side Wrap</title>
<link href="https://fonts.googleapis.com/css2?family=Oswald:wght@500;600;700&family=Cinzel:wght@500&display=swap" rel="stylesheet">
<style>
  :root {
    --bg: #eef0ea;
    --band: #0f6b1c;
    --grass-dark: #2f9a1c;
    --grass-light: #acd037;
    --white: #ffffff;
    --gold: #e8c46a;
  }
  html, body {
    margin: 0;
    width: 1200px;
    height: 800px;
    overflow: hidden;
    background: var(--bg);
  }
  .wrap-panel {
    position: absolute;
    left: 50px;
    top: 265px;
    width: 1100px;
    height: 270px;
  }
  .wrap-panel svg.panel-shape {
    position: absolute;
    inset: 0;
  }
  .sod-roll {
    position: absolute;
    left: 0;
    top: 0;
    width: 175px;
    height: 270px;
    background: linear-gradient(160deg, #7fbf3a 0%, #3f8f1e 55%, #2d6a14 100%);
    border-radius: 0 60px 40px 0;
  }
  .phone {
    position: absolute;
    left: 200px;
    top: 12px;
    display: flex;
    align-items: center;
    gap: 10px;
    font-family: 'Oswald', sans-serif;
    font-weight: 600;
    font-size: 44px;
    line-height: 1;
    color: var(--white);
  }
  .phone svg { width: 34px; height: 34px; }
  .brand {
    position: absolute;
    left: 575px;
    top: 12px;
    display: flex;
    align-items: center;
    gap: 14px;
  }
  .brand-name {
    font-family: 'Oswald', sans-serif;
    font-weight: 500;
    font-size: 25px;
    line-height: 1.05;
    color: var(--gold);
    text-transform: uppercase;
    letter-spacing: 1px;
  }
  .brand-dot {
    width: 30px;
    height: 30px;
    border-radius: 50%;
    background: var(--gold);
  }
  .headline {
    position: absolute;
    left: 200px;
    top: 88px;
    font-family: 'Oswald', sans-serif;
    font-weight: 700;
    color: var(--white);
    text-transform: uppercase;
    line-height: 1;
  }
  .headline .sod {
    display: block;
    font-size: 128px;
    letter-spacing: 10px;
    line-height: 0.95;
  }
  .headline .landscape {
    display: block;
    font-size: 38px;
    letter-spacing: 0.5px;
  }
  .services {
    position: absolute;
    left: 440px;
    top: 92px;
    font-family: 'Oswald', sans-serif;
    font-weight: 600;
    font-size: 42px;
    line-height: 1.12;
    color: var(--white);
    text-transform: uppercase;
  }
  .credentials {
    position: absolute;
    left: 442px;
    top: 196px;
    display: flex;
    gap: 20px;
    padding: 4px 10px;
    border: 2px solid var(--white);
    font-family: 'Oswald', sans-serif;
    font-weight: 500;
    font-size: 20px;
    color: var(--white);
    text-transform: uppercase;
  }
</style>
</head>
<body>
  <section class="wrap-panel">
    <svg class="panel-shape" viewBox="0 0 1100 270" width="1100" height="270">
      <defs>
        <linearGradient id="grass" x1="0" y1="0" x2="1" y2="1">
          <stop offset="0" stop-color="#acd037"/>
          <stop offset="0.6" stop-color="#4fae24"/>
          <stop offset="1" stop-color="#2f9a1c"/>
        </linearGradient>
        <clipPath id="panel-clip">
          <path d="M0,0 H960 Q1050,8 1100,35 V150 Q1030,165 1000,270 H0 Z"/>
        </clipPath>
      </defs>
      <g clip-path="url(#panel-clip)">
        <rect width="1100" height="270" fill="url(#grass)"/>
        <rect width="1100" height="80" fill="#0f6b1c"/>
      </g>
    </svg>

    <div class="sod-roll" role="img" aria-label="Photo of a rolled-up strip of fresh green sod"></div>

    <div class="phone">
      <svg viewBox="0 0 24 24" aria-hidden="true"><path fill="#e8c46a" d="M6.6 10.8a15.1 15.1 0 0 0 6.6 6.6l2.2-2.2a1 1 0 0 1 1-.25 11.4 11.4 0 0 0 3.6.57 1 1 0 0 1 1 1V20a1 1 0 0 1-1 1A17 17 0 0 1 3 4a1 1 0 0 1 1-1h3.5a1 1 0 0 1 1 1c0 1.25.2 2.45.57 3.57a1 1 0 0 1-.25 1z"/></svg>
      <span>555-317-4486</span>
    </div>

    <div class="brand">
      <div class="brand-name">Tarnwell<br>Outfitters</div>
      <div class="brand-dot"></div>
    </div>

    <h1 class="headline">
      <span class="sod">SOD</span>
      <span class="landscape">&amp; Landscape</span>
    </h1>

    <div class="services">Installation<br>&amp; Delivery</div>

    <div class="credentials">
      <span>✓ Licensed</span>
      <span>✓ Insured</span>
    </div>
  </section>
</body>
</html>
```